Design a Website for an IT Support Company

We are an IT support company that provides commercial IT support and services to small and medium sized businesses. We are in need of a website to be developed for our business.
We would like to work with someone who is either familiar with the IT field, or has developed a website for an IT support company in the past.
Some examples of designs/layouts that we like:
https://www.velmorask.example/
http://www.quibenstack.example/
http://572zo.example/
http://www.guspelnetworks.example/
http://www.ourba.example/
I have attached a word document that gives a menu system/page layout format that we would like for our website as well as branch office phone numbers. Our logo is also attached that you can use for your design purposes. We currently do not have copy produced for all of the pages outlined in the word document, but would get this done during the project with the selected designer.
We would like the website to be SEO friendly & fully responsive. We would prefer a Wordpress format, however, we are open to HTML formats as well.

```html
<!DOCTYPE html>
<html lang="en">
<head>
<meta charset="utf-8">
<title>Corvane IT</title>
<link rel="stylesheet" href="https://fonts.googleapis.com/css2?family=Nunito:wght@300;400;600;700&display=swap">
<style>
:root{
  --navy:#062f6b;
  --deep:#0a4a8a;
  --teal:#0a82b4;
  --sky:#19b3e6;
  --sky-soft:#2ec0ef;
  --ink:#1b1b1b;
  --muted:#9aa3ad;
  --line:#e6eaee;
  --white:#ffffff;
}
*{box-sizing:border-box;margin:0;padding:0}
html,body{width:1200px;height:3136px;overflow:hidden}
body{position:relative;font-family:"Nunito",sans-serif;color:var(--ink);background:var(--white)}
.abs{position:absolute}
.accent{color:var(--sky)}

/* hero */
.hero{left:0;top:0;width:1200px;height:625px;background:linear-gradient(135deg,#0a6fa6 0%,#075b95 45%,#043c78 100%);overflow:hidden}
.hero-shade{left:0;top:390px;width:620px;height:235px;background:rgba(0,30,80,.25)}
.hero-triangle{left:905px;top:85px;width:265px;height:220px}
.brand{left:115px;top:14px;display:flex;align-items:center;gap:8px;color:var(--white);font-weight:700;font-size:18px}
.brand-dot{width:26px;height:26px;border:2px solid var(--white);border-radius:50%}
.nav{top:21px;left:0;width:1200px;height:20px}
.nav a{position:absolute;color:var(--white);text-decoration:none;font-size:13px}
.devices{left:95px;top:110px;width:330px;height:410px;border-radius:22px;background:linear-gradient(160deg,#e9eef2 0%,#b9c6d0 55%,#6d8aa3 100%)}
.hero-title{left:556px;top:292px;color:var(--white);font-size:50px;font-weight:700;letter-spacing:.5px}
.hero-copy{left:556px;top:364px;width:400px;color:var(--white);font-size:13px;font-weight:600;line-height:1.45}
.read-more{display:flex;align-items:center;gap:14px;font-size:12px;padding-bottom:6px;border-bottom:1px solid currentColor}
.hero .read-more{left:556px;top:466px;color:var(--white)}

/* services */
.section-title{left:0;width:1200px;text-align:center;font-size:40px;font-weight:600}
.services-title{top:660px;color:var(--ink)}
.services-sub{left:0;top:716px;width:1200px;text-align:center;font-size:28px;font-weight:300;color:#333}
.rule{height:1px;background:var(--sky)}
.service{display:flex;align-items:center;gap:22px;font-size:15px;color:#333}
.service.right{flex-direction:row-reverse}
.icon{width:58px;height:58px;border-radius:50%;background:var(--sky);display:flex;align-items:center;justify-content:center;flex:none}
.slide-arrow{top:940px}

/* why */
.why{left:0;top:1227px;width:1200px;height:660px;background:linear-gradient(160deg,#0a89b8 0%,#0a5f9c 45%,#06306d 100%)}
.why-title{top:1280px;color:var(--white)}
.why-sub{left:0;top:1350px;width:1200px;text-align:center;color:var(--sky-soft);font-size:14px}
.screen{border-radius:3px}
.screen.side{background:linear-gradient(180deg,#6b85a8 0%,#48618a 100%);opacity:.85}
.screen.far{opacity:.4}
.screen.main{background:linear-gradient(180deg,#f6f7f9,#e8ebef)}
.dot{width:10px;height:10px;border-radius:50%;background:var(--sky)}

/* reviews */
.reviews-title{left:160px;top:1923px;font-size:30px;font-weight:600}
.reviews-sub{left:160px;top:1984px;font-size:13px;color:var(--muted)}
.quote{font-size:90px;line-height:1;color:var(--sky);font-weight:700}
.avatar{width:96px;height:96px;border-radius:50%;background:linear-gradient(160deg,#c8b7a6,#7b6a5e)}
.reviewer{font-size:15px;font-weight:700;color:#222}
.date{font-size:13px;color:var(--sky)}
.review-text{width:712px;font-size:13px;line-height:1.6;color:var(--muted);font-style:italic}
.divider{height:1px;background:var(--line)}
.reviews-more{left:530px;top:2412px;color:var(--sky)}

/* contact */
.contact{left:0;top:2498px;width:1200px;height:638px;background:linear-gradient(160deg,#0a6aa4 0%,#0a4c8e 40%,#051f5c 100%)}
.contact-title{top:2552px;color:var(--white)}
.contact-sub{left:0;top:2620px;width:1200px;text-align:center;color:var(--sky-soft);font-size:14px}
.field{left:168px;width:240px;height:36px;border:1px solid rgba(120,170,220,.45);color:var(--white);font-size:13px;padding:9px 14px}
.submit{left:168px;top:2918px;width:240px;height:36px;background:#1d87c0;color:var(--white);font-size:13px;font-weight:700;text-align:center;line-height:36px}
.map{left:592px;top:2686px;width:438px;height:302px;background:linear-gradient(135deg,#efe6d2 0%,#e6dcc4 50%,#f1c98e 100%)}
.footer-rule{left:0;top:3070px;width:1200px;height:1px;background:rgba(255,255,255,.15)}
.social{top:3101px;width:20px;height:20px;border-radius:50%;background:rgba(255,255,255,.85)}
</style>
</head>
<body>

<section class="abs hero" aria-label="Intro">
  <div class="abs hero-shade"></div>
  <svg class="abs hero-triangle" viewBox="0 0 265 220"><rect width="265" height="220" fill="#0a99cf" opacity=".55"/><polygon points="0,0 265,220 0,220" fill="#18b0e4"/><polygon points="0,0 265,0 265,220" fill="#0e9bd3" opacity=".7"/></svg>
  <div class="abs brand"><span class="brand-dot"></span>Corvane IT</div>
  <nav class="abs nav">
    <a style="left:528px" href="#">Home</a>
    <a style="left:622px" href="#">Services</a>
    <a style="left:735px" href="#">Why Corvane IT</a>
    <a style="left:890px" href="#">Contact</a>
    <svg style="position:absolute;left:1013px;top:0" width="20" height="20" viewBox="0 0 20 20"><circle cx="8" cy="8" r="6" fill="none" stroke="#fff" stroke-width="2"/><line x1="12.5" y1="12.5" x2="18" y2="18" stroke="#fff" stroke-width="2"/></svg>
  </nav>
  <div class="abs devices" role="img" aria-label="Tablet and phone showing the company's apps"></div>
  <h1 class="abs hero-title">CorvaneIT</h1>
  <p class="abs hero-copy">Lorem ipsum dolor sit amet, consectetur adipiscing elit. Nunc tempus purus elit, non sollicitudin metus porta aliquet.</p>
  <a class="abs read-more">Read more
    <svg width="18" height="10" viewBox="0 0 18 10"><path d="M0 5h16M12 1l4 4-4 4" fill="none" stroke="currentColor" stroke-width="1.5"/></svg></a>
</section>

<section aria-label="Services">
  <h2 class="abs section-title services-title">Our <span class="accent">services</span></h2>
  <div class="abs rule" style="left:228px;top:738px;width:276px"></div>
  <div class="abs services-sub">Data</div>
  <div class="abs rule" style="left:726px;top:738px;width:248px"></div>

  <div class="abs service" style="left:221px;top:786px"><span class="icon"><svg width="26" height="22"><rect x="2" y="5" width="22" height="15" rx="2" fill="none" stroke="#fff" stroke-width="2"/></svg></span>Managed IT Services</div>
  <div class="abs service" style="left:221px;top:873px"><span class="icon"><svg width="26" height="22"><rect x="3" y="3" width="20" height="14" fill="#f08a24"/></svg></span>IT Support &amp; Consulting</div>
  <div class="abs service" style="left:221px;top:960px"><span class="icon"><svg width="24" height="24"><circle cx="12" cy="12" r="10" fill="#fff"/><path d="M12 12V2a10 10 0 0 1 10 10z" fill="#f5b400"/></svg></span>IT Helpdesk Services</div>
  <div class="abs service" style="left:216px;top:1046px"><span class="icon"><svg width="22" height="24"><rect x="3" y="10" width="16" height="12" fill="#fff"/><path d="M6 10V6a5 5 0 0 1 10 0v4" fill="none" stroke="#fff" stroke-width="2"/></svg></span>Network Security</div>
  <div class="abs service" style="left:216px;top:1131px"><span class="icon"><svg width="22" height="24"><rect x="3" y="10" width="16" height="12" fill="#fff"/><path d="M6 10V6a5 5 0 0 1 10 0v4" fill="none" stroke="#fff" stroke-width="2"/></svg></span>Email &amp; Spam Threat Management</div>

  <div class="abs service right" style="right:226px;top:786px"><span class="icon"><svg width="24" height="24"><circle cx="12" cy="12" r="9" fill="#f08a24"/><circle cx="12" cy="12" r="4" fill="#fff"/></svg></span>Wireless Networking</div>
  <div class="abs service right" style="right:226px;top:873px"><span class="icon"><svg width="28" height="20"><rect x="2" y="4" width="24" height="12" rx="6" fill="#1a2a48"/></svg></span>Remote Monitoring Services</div>
  <div class="abs service right" style="right:226px;top:960px"><span class="icon"><svg width="22" height="24"><path d="M11 2l9 3v7c0 5-4 9-9 10-5-1-9-5-9-10V5z" fill="#8bc34a"/></svg></span>Servers &amp; Virtualization</div>
  <div class="abs service right" style="right:226px;top:1046px"><span class="icon"><svg width="24" height="24"><path d="M4 20L18 4l2 2L6 22z" fill="#f5a623"/></svg></span>Data Backup &amp; Recovery</div>
  <div class="abs service right" style="right:226px;top:1131px"><span class="icon"><svg width="24" height="24"><circle cx="12" cy="12" r="9" fill="#f08a24"/><circle cx="12" cy="12" r="4" fill="#fff"/></svg></span>Structured Cabling</div>

  <svg class="abs slide-arrow" style="left:65px" width="50" height="44" viewBox="0 0 50 44"><path d="M48 22H4M22 4L4 22l18 18" fill="none" stroke="#19b3e6" stroke-width="3"/></svg>
  <svg class="abs slide-arrow" style="left:1095px" width="50" height="44" viewBox="0 0 50 44"><path d="M2 22h44M28 4l18 18-18 18" fill="none" stroke="#19b3e6" stroke-width="3"/></svg>
</section>

<section class="abs why" aria-label="Why Corvane IT"></section>
<h2 class="abs section-title why-title"><span class="accent">Why</span> Corvane IT</h2>
<div class="abs rule" style="left:420px;top:1338px;width:360px;opacity:.6"></div>
<p class="abs why-sub">Lorem ipsum dolor sit amet, consectetur adipiscing elit</p>
<div class="abs screen side" style="left:80px;top:1445px;width:160px;height:290px" role="img" aria-label="Weather app screen"></div>
<div class="abs screen side" style="left:292px;top:1445px;width:160px;height:290px" role="img" aria-label="App menu screen"></div>
<div class="abs screen main" style="left:500px;top:1420px;width:190px;height:340px" role="img" aria-label="App sign-in screen"></div>
<div class="abs screen side" style="left:743px;top:1445px;width:160px;height:290px" role="img" aria-label="Weather app screen"></div>
<div class="abs screen side far" style="left:960px;top:1445px;width:160px;height:290px" role="img" aria-label="Calendar app screen"></div>
<div class="abs dot" style="left:565px;top:1812px;width:7px;height:7px"></div>
<div class="abs dot" style="left:592px;top:1808px;width:15px;height:15px"></div>
<div class="abs dot" style="left:623px;top:1812px;width:7px;height:7px"></div>

<section aria-label="Reviews">
  <h2 class="abs reviews-title">Our <span class="accent">reviews</span></h2>
  <div class="abs rule" style="left:160px;top:1970px;width:308px"></div>
  <p class="abs reviews-sub">Lorem ipsum dolor sit amet, consectetur adipiscing elit</p>

  <div class="abs quote" style="left:150px;top:2042px">“</div>
  <div class="abs avatar" style="left:166px;top:2070px" role="img" aria-label="Portrait of Lena Ostrow"></div>
  <div class="abs reviewer" style="left:280px;top:2068px">Lena Ostrow</div>
  <div class="abs date" style="left:968px;top:2068px">21.01.2017</div>
  <p class="abs review-text" style="left:280px;top:2100px">Lorem ipsum dolor sit amet, consectetur adipiscing elit. Nunc tempus purus elit, non sollicitudin metus porta aliquet. Lorem ipsum dolor sit amet, consectetur adipiscing elit. Nunc tempus purus elit, non sollicitudin metus porta aliquet. Lorem ipsum dolor sit amet, consectetur adipiscing elit. Nunc tempus purus elit, non sollicitudin metus porta aliquet.</p>
  <div class="abs divider" style="left:160px;top:2205px;width:872px"></div>

  <div class="abs quote" style="left:150px;top:2218px">“</div>
  <div class="abs avatar" style="left:166px;top:2246px" role="img" aria-label="Portrait of Tomas Berrin"></div>
  <div class="abs reviewer" style="left:280px;top:2244px">Tomas Berrin</div>
  <div class="abs date" style="left:968px;top:2244px">21.01.2017</div>
  <p class="abs review-text" style="left:280px;top:2276px">Lorem ipsum dolor sit amet, consectetur adipiscing elit. Nunc tempus purus elit, non sollicitudin metus porta aliquet. Lorem ipsum dolor sit amet, consectetur adipiscing elit. Nunc tempus purus elit, non sollicitudin metus porta aliquet. Lorem ipsum dolor sit amet, consectetur adipiscing elit. Nunc tempus purus elit, non sollicitudin metus porta aliquet.</p>
  <div class="abs divider" style="left:160px;top:2385px;width:872px"></div>

  <a class="abs read-more reviews-more">Read more
    <svg width="18" height="10" viewBox="0 0 18 10"><path d="M0 5h16M12 1l4 4-4 4" fill="none" stroke="currentColor" stroke-width="1.5"/></svg></a>
</section>

<section class="abs contact" aria-label="Contact"></section>
<h2 class="abs section-title contact-title">Our <span class="accent">contact</span></h2>
<div class="abs rule" style="left:420px;top:2610px;width:360px;opacity:.6"></div>
<p class="abs contact-sub">Lorem ipsum dolor sit amet, consectetur adipiscing elit</p>
<div class="abs field" style="top:2685px">Name</div>
<div class="abs field" style="top:2741px">Phone number</div>
<div class="abs field" style="top:2797px">E-mail</div>
<div class="abs field" style="top:2852px">Your text</div>
<div class="abs submit">Submit</div>
<div class="abs map" role="img" aria-label="Street map with office location pin"></div>
<div class="abs footer-rule"></div>
<div class="abs social" style="left:908px"></div>
<div class="abs social" style="left:942px"></div>
<div class="abs social" style="left:976px"></div>
<div class="abs social" style="left:1010px"></div>

</body>
</html>
```